ARC VOLLEY Business Card Project

I'd like to request a business card design for the new company I've launched.
The name of the company is "ARC VOLLEY" an indoor unmanned tennis practice facility.
We would like to see designs that use our brand identity color in the logo I've attached.
We hope to get the design with modern, luxurious and elegant tone and manner.
We hope the logo should not be too big.

Business card must have elements as below:
- Logo (One of the logos I've attached)
- Name (In Korean Text) : 박 서 윤
- Title (In Korean Text) : 대표
- Phone Number : 010-8472-3916
- Email Address : seoyun.park@arcvolley-example.co.kr
- Website : www.arcvolley-example.co.kr
- Instagram : arcvolley
- Address (In Korean text) : 강원도 가온시 새빛구 하람로 456 미래타워 5층 501호, 502호

Target Market(s)

Tennis amateurs in 20 to 40s

Industry/Entity Type

Sports, Hobby

Contact Information for Business Card

- Logo (One of the logos I've attached) - Name (In Korean Text) : 박 서 윤 - Title (In Korean Text) : 대표 - Phone Number : 010-8472-3916 - Email Address : seoyun.park@arcvolley-example.co.kr - Website : www.arcvolley-example.co.kr - Instagram : arcvolley - Address (In Korean text) : 강원도 가온시 새빛구 하람로 456 미래타워 5층 501호, 502호

Font styles to use
Sans Serif

Requirements
Must have
• Double sided
Nice to have
• Logo with intaglio or relief embossing
Should not have
• Logo should not be too big.

```html
<!DOCTYPE html>
<html lang="ko">
<head>
<meta charset="utf-8">
<title>ARC VOLLEY Business Cards</title>
<link href="https://fonts.googleapis.com/css2?family=Noto+Sans+KR:wght@400;500&display=swap" rel="stylesheet">
<style>
  :root {
    --backdrop: #7b7c7e;
    --brand-green: #2f5a3c;
    --paper: #ffffff;
    --ink-green: #2f5a3c;
    --ink-light: #ffffff;
  }
  * { box-sizing: border-box; margin: 0; padding: 0; }
  html, body { width: 847px; height: 1200px; overflow: hidden; }
  body {
    background: var(--backdrop);
    font-family: "Noto Sans KR", sans-serif;
    position: relative;
  }
  .card {
    position: absolute;
    width: 316px; height: 190px;
    overflow: hidden;
  }
  .card--light { background: var(--paper); color: var(--ink-green); width: 286px; left: 91px; top: 686px; }
  .card--front-dark { left: 91px; top: 947px; }
  .card--back-top { left: 440px; top: 686px; }
  .card--back-bottom { left: 440px; top: 947px; }
  .card--dark { background: var(--brand-green); color: var(--ink-light); }

  .brand {
    display: flex; align-items: center; gap: 6px;
    font-weight: 400; letter-spacing: 0.04em; white-space: nowrap;
  }
  .brand__dot { border: 2px solid currentColor; border-radius: 50%; flex: none; }
  .card__front-brand {
    position: absolute; left: 97px; top: 14px;
    font-size: 18px;
  }
  .card--front-dark .card__front-brand { left: 115px; }
  .card__front-brand .brand__dot { width: 34px; height: 34px; }

  .card__back-brand {
    position: absolute; left: 0; right: 0; top: 62px;
    flex-direction: column; gap: 8px;
    font-size: 19px;
  }
  .card__back-brand .brand__dot { width: 42px; height: 42px; }

  .holder {
    position: absolute; left: 23px; top: 72px;
    font-size: 13px; line-height: 19px;
  }
  .contact-list {
    position: absolute; left: 23px; top: 113px;
    list-style: none;
    font-size: 10px; line-height: 12px;
    white-space: nowrap;
  }
  .contact-list li { display: flex; align-items: center; gap: 6px; }
  .contact-list svg { width: 8px; height: 8px; flex: none; fill: currentColor; }
  .contact-list .address { font-size: 8.5px; margin-top: 3px; }
</style>
</head>
<body>

  <section class="card card--light" aria-label="Card front, white">
    <div class="brand card__front-brand"><span class="brand__dot"></span>ARC VOLLEY</div>
    <div class="holder"><p>박 서 윤</p><p>대표</p></div>
    <ul class="contact-list">
      <li><svg viewBox="0 0 10 10"><path d="M2 0.5 L3.8 2.6 L2.9 3.8 Q4 6 6.2 7.1 L7.4 6.2 L9.5 8 L8.3 9.5 Q2 9 0.5 1.7 Z"/></svg>010-8472-3916</li>
      <li><svg viewBox="0 0 10 10"><path d="M0 2 H10 V8.5 H0 Z M0.6 2.4 L5 5.6 L9.4 2.4" fill="none" stroke="currentColor" stroke-width="1.2"/></svg>seoyun.park@arcvolley-example.co.kr</li>
      <li><svg viewBox="0 0 10 10"><g fill="none" stroke="currentColor" stroke-width="1"><circle cx="5" cy="5" r="4.3"/><ellipse cx="5" cy="5" rx="1.9" ry="4.3"/><path d="M0.7 5 H9.3"/></g></svg>www.arcvolley-example.co.kr</li>
      <li><svg viewBox="0 0 10 10"><circle cx="5" cy="5" r="4.3"/></svg>@arcvolley</li>
      <li class="address"><svg viewBox="0 0 10 10"><path d="M5 0.3 A3.4 3.4 0 0 1 8.4 3.7 Q8.4 6 5 9.8 Q1.6 6 1.6 3.7 A3.4 3.4 0 0 1 5 0.3 Z M5 2.4 A1.3 1.3 0 1 0 5 5 A1.3 1.3 0 1 0 5 2.4 Z" fill-rule="evenodd"/></svg>강원도 가온시 새빛구 하람로 456 미래타워 5층 501호, 502호</li>
    </ul>
  </section>

  <section class="card card--dark card--back-top" aria-label="Card back, green">
    <div class="brand card__back-brand"><span class="brand__dot"></span>ARC VOLLEY</div>
  </section>

  <section class="card card--dark card--front-dark" aria-label="Card front, green">
    <div class="brand card__front-brand"><span class="brand__dot"></span>ARC VOLLEY</div>
    <div class="holder"><p>박 서 윤</p><p>대표</p></div>
    <ul class="contact-list">
      <li><svg viewBox="0 0 10 10"><path d="M2 0.5 L3.8 2.6 L2.9 3.8 Q4 6 6.2 7.1 L7.4 6.2 L9.5 8 L8.3 9.5 Q2 9 0.5 1.7 Z"/></svg>010-8472-3916</li>
      <li><svg viewBox="0 0 10 10"><path d="M0 2 H10 V8.5 H0 Z M0.6 2.4 L5 5.6 L9.4 2.4" fill="none" stroke="currentColor" stroke-width="1.2"/></svg>seoyun.park@arcvolley-example.co.kr</li>
      <li><svg viewBox="0 0 10 10"><g fill="none" stroke="currentColor" stroke-width="1"><circle cx="5" cy="5" r="4.3"/><ellipse cx="5" cy="5" rx="1.9" ry="4.3"/><path d="M0.7 5 H9.3"/></g></svg>www.arcvolley-example.co.kr</li>
      <li><svg viewBox="0 0 10 10"><circle cx="5" cy="5" r="4.3"/></svg>@arcvolley</li>
      <li class="address"><svg viewBox="0 0 10 10"><path d="M5 0.3 A3.4 3.4 0 0 1 8.4 3.7 Q8.4 6 5 9.8 Q1.6 6 1.6 3.7 A3.4 3.4 0 0 1 5 0.3 Z M5 2.4 A1.3 1.3 0 1 0 5 5 A1.3 1.3 0 1 0 5 2.4 Z" fill-rule="evenodd"/></svg>강원도 가온시 새빛구 하람로 456 미래타워 5층 501호, 502호</li>
    </ul>
  </section>

  <section class="card card--dark card--back-bottom" aria-label="Card back, green">
    <div class="brand card__back-brand"><span class="brand__dot"></span>ARC VOLLEY</div>
  </section>

</body>
</html>
```